bright lane coaching needs snazzy business card that serves a dual purpose

business card needed for a Bright Lane Coaching company that takes people out on the road to teach them proficiency on their bike.
My business logo is attached. I have grey and aqua colours with my logo.
i really like bitumen/tarmac/ road in the design somehow but that is up to you.
I think navy blue will go well with my colours too. see how you go.

I want this card to look REALLY good.
the back of the card may be used for emergency contact details too
In case of Emergency I am:
Name:

Emergency Contact name
emergency contact Phone number:

• details that are essential are:
• logo
• Name: Marnie HOLT
• ABN: 53 916 204 871
• phone number: 0438 152 964
• facebook logo
• * ride tuition & proficiency
• * skills practice
• * maintenance 101
• * bike fitting service
• * cater for all ages & abilities
• backpage:
• logo
• skills confidence enjoyment
• some space for writing
• nothing girly. The business will already naturally attract women, it needs to appeal to both genders

```html
<!DOCTYPE html>
<html lang="en">
<head>
<meta charset="utf-8">
<title>Bright Lane Coaching – Business Card</title>
<link rel="stylesheet" href="https://fonts.googleapis.com/css2?family=Didact+Gothic&family=Open+Sans:ital,wght@0,400;1,400&display=swap">
<style>
  :root {
    --aqua: #5ec4b4;
    --aqua-soft: #a5ddd4;
    --ink: #2e2e2e;
    --rule: #9a9a9a;
    --card: #ffffff;
    --bg-grey: #b9b9b9;
    --bg-cream: #f4f0c9;
    --bar-dark: #3a6f69;
  }
  html, body { margin: 0; padding: 0; overflow: hidden; }
  body {
    width: 846px; height: 1200px; position: relative;
    background: linear-gradient(105deg, var(--bg-grey) 0%, #d8d7bd 35%, var(--bg-cream) 62%, var(--bg-cream) 100%);
    font-family: "Didact Gothic", "Century Gothic", sans-serif;
    color: var(--ink);
  }
  .card { position: absolute; background: var(--card); overflow: hidden; }
  .card--front { left: 176px; top: 261px; width: 508px; height: 296px; }
  .card--back { left: 177px; top: 642px; width: 508px; height: 297px; }

  .wordmark { position: absolute; display: flex; align-items: center; gap: 8px; white-space: nowrap; color: var(--ink); }
  .wordmark__dot { border-radius: 50%; background: var(--aqua); flex: none; }
  .card--front .wordmark { left: 0; right: 0; top: 46px; justify-content: center; font-size: 28px; }
  .card--front .wordmark__dot { width: 14px; height: 14px; }
  .card--back .wordmark { left: 40px; top: 132px; font-size: 19px; }
  .card--back .wordmark__dot { width: 10px; height: 10px; }

  .header-rule { position: absolute; left: 107px; top: 107px; width: 296px; height: 1.5px; background: var(--rule); }
  .owner-name { position: absolute; left: 0; right: 0; top: 110px; text-align: center; font-size: 21px; letter-spacing: 0.3px; }
  .owner-abn { position: absolute; left: 0; right: 0; top: 136px; text-align: center; font-size: 7px; }

  .accent-bar { position: absolute; left: 24px; top: 159px; width: 3px; height: 117px; background: var(--aqua); }
  .accent-bar::before { content: ""; position: absolute; left: 0; top: 0; width: 3px; height: 10px; background: var(--bar-dark); }

  .contact { position: absolute; display: flex; align-items: center; gap: 6px; font-size: 15px; }
  .card--front .contact--phone { left: 44px; top: 183px; }
  .social-square { position: absolute; left: 46px; top: 218px; width: 15px; height: 15px; background: var(--aqua); }
  .phone-icon { width: 17px; height: 17px; flex: none; }

  .services { position: absolute; right: 19px; top: 177px; margin: 0; padding: 0; list-style: none;
    text-align: right; font-family: "Open Sans", sans-serif; font-size: 11px; line-height: 15px; }

  .divider { position: absolute; left: 258px; top: 56px; width: 3px; height: 184px; background: var(--aqua-soft); }
  .wedge { position: absolute; left: 0; top: 0; width: 508px; height: 297px; }
  .tagline { position: absolute; left: 287px; top: 116px; font-family: "Open Sans", sans-serif; font-size: 11.5px; }
  .card--back .contact--phone { left: 277px; top: 138px; font-family: "Open Sans", sans-serif; font-size: 12px; gap: 4px; }
  .card--back .phone-icon { width: 15px; height: 15px; }
  .note-label { position: absolute; left: 277px; top: 163px; font-family: "Open Sans", sans-serif; font-style: italic; font-size: 7px; }
  .note-line { position: absolute; height: 1px; background: #6f7e7b; }
</style>
</head>
<body>

<section class="card card--front">
  <div class="wordmark"><span class="wordmark__dot"></span>Bright Lane Coaching</div>
  <div class="header-rule"></div>
  <div class="owner-name">Marnie HOLT</div>
  <div class="owner-abn">53 916 204 871</div>

  <div class="accent-bar"></div>
  <div class="contact contact--phone">
    <svg class="phone-icon" viewBox="0 0 20 20" aria-hidden="true">
      <circle cx="10" cy="10" r="8.5" fill="none" stroke="var(--aqua)" stroke-width="1.6"/>
      <path d="M7 5.5c-1.3.8-1.6 2.2-.8 3.9.9 2 2.5 3.8 4.3 4.7 1.5.7 2.7.4 3.4-.6l-1.7-1.5-1.2.6c-1-.5-2-1.6-2.5-2.7l.8-1.1z" fill="var(--aqua)"/>
    </svg>
    <span>0438 152 964</span>
  </div>
  <div class="social-square" aria-hidden="true"></div>

  <ul class="services">
    <li>- Ride tuition &amp; proficiency</li>
    <li>- Skills practice</li>
    <li>- Maintenance 101</li>
    <li>- Bike fitting service</li>
    <li>- Cater for all ages &amp; abilities</li>
  </ul>
</section>

<section class="card card--back">
  <svg class="wedge" viewBox="0 0 508 297" aria-hidden="true">
    <polygon points="261,145 508,21 508,269" fill="var(--aqua-soft)"/>
  </svg>
  <div class="wordmark"><span class="wordmark__dot"></span>Bright Lane Coaching</div>
  <div class="divider"></div>
  <div class="tagline">Get it better and enjoy with us</div>
  <div class="contact contact--phone">
    <svg class="phone-icon" viewBox="0 0 20 20" aria-hidden="true">
      <circle cx="10" cy="10" r="8.5" fill="none" stroke="var(--aqua)" stroke-width="1.6"/>
      <path d="M7 5.5c-1.3.8-1.6 2.2-.8 3.9.9 2 2.5 3.8 4.3 4.7 1.5.7 2.7.4 3.4-.6l-1.7-1.5-1.2.6c-1-.5-2-1.6-2.5-2.7l.8-1.1z" fill="var(--aqua)"/>
    </svg>
    <span>0438 152 964</span>
  </div>
  <div class="note-label">Note :</div>
  <div class="note-line" style="left:301px; top:171px; width:162px;"></div>
  <div class="note-line" style="left:296px; top:183px; width:167px;"></div>
  <div class="note-line" style="left:296px; top:195px; width:167px;"></div>
</section>

</body>
</html>
```